Breast Cancer Month Banner

I need a standing banner and a n outdoor banner design
Please include the logos of the sponsors at the bottom or the top
I've include the logos in one file called Back Design and Orchard Lane Logo
12Ft x 3Ft - horizontal banner - This can be a regular banner depicting Breast cancer awareness month #Pinktober. some examples have been attached
2.5Ft x 6Ft - Standing banner - THis banner should be an Infographic type banner depicting breast cancer causes, risk factors and prevention. examples of info graphic have been attached

```html
<!DOCTYPE html>
<html lang="en">
<head>
<meta charset="utf-8">
<title>Breast Cancer Awareness</title>
<link href="https://fonts.googleapis.com/css2?family=Didact+Gothic&family=Montserrat:wght@700;800&family=Barlow:wght@500;600&display=swap" rel="stylesheet">
<style>
:root{
  --bg-top:#f4a0c5;
  --bg-bottom:#fbeff5;
  --frame:#9c2e6c;
  --accent:#e8629a;
  --accent-soft:#f07fab;
  --ink:#1a1a1a;
  --deep:#8a1b52;
  --white:#ffffff;
}
*{margin:0;padding:0;box-sizing:border-box}
html,body{width:1200px;height:2880px;overflow:hidden}
body{
  position:relative;
  background:linear-gradient(180deg,var(--bg-top) 0%,#f7bcd6 40%,var(--bg-bottom) 100%);
  font-family:"Didact Gothic",sans-serif;
  color:var(--ink);
}
.abs{position:absolute}
.art{position:absolute}

/* header */
.title-frame{left:142px;top:182px;width:915px;height:310px;border:13px solid var(--frame);box-shadow:0 0 30px rgba(255,255,255,.6)}
.ribbon{left:212px;top:78px;width:336px;height:520px;border-radius:160px 160px 40px 40px;
  background:linear-gradient(160deg,#f7b3cc,#ec6c9d 55%,#f4a2c0)}
.title{left:442px;top:280px;width:600px;text-align:center;color:var(--white);white-space:nowrap;
  font-family:"Montserrat",sans-serif;font-weight:800;font-size:60px;line-height:64px;letter-spacing:.5px}

/* stats */
.women{left:93px;top:640px;width:317px;height:342px;border-radius:12px;
  background:linear-gradient(90deg,#ee6e9f 0%,#ee6e9f 75%,#8e1c56 75%)}
.big-ratio{left:98px;top:1010px;font-family:"Barlow",sans-serif;font-weight:600;font-size:64px;line-height:66px;letter-spacing:1px;white-space:nowrap}
.stat-text{font-size:27px;line-height:30px;white-space:nowrap}
.ratio-text{left:98px;top:1090px}
.divider-v{left:469px;top:632px;width:4px;height:578px;background:var(--accent)}
.world-map{left:509px;top:587px;width:570px;height:285px;border-radius:40px;
  background:linear-gradient(180deg,#f07fab,#f6a9c7)}
.stat .every{font-family:"Barlow",sans-serif;font-size:26px;line-height:26px}
.stat .num{font-family:"Barlow",sans-serif;font-weight:600;font-size:118px;line-height:100px;letter-spacing:-4px}
.stat .unit{font-family:"Barlow",sans-serif;font-size:19px;line-height:22px;margin-bottom:14px}
.stat-a{left:512px;top:888px}
.stat-b{left:693px;top:888px}
.flag{left:873px;top:915px;width:200px;height:105px;background:linear-gradient(135deg,#3c3b6e,#c9283b)}
.flag-text{left:873px;top:1058px}

.rule{left:69px;width:1030px;height:4px;background:var(--accent)}
.section-title{left:0;width:1200px;text-align:center;font-family:"Barlow",sans-serif;font-weight:500;font-size:80px;line-height:80px;letter-spacing:2px}

/* items */
.item{white-space:nowrap}
.item h3{font-family:"Didact Gothic",sans-serif;font-weight:400;color:var(--accent);font-size:27px;line-height:30px;text-transform:uppercase;-webkit-text-stroke:.8px var(--accent)}
.item p{font-size:27px;line-height:30px}
.icon{position:absolute;background:var(--accent-soft);border-radius:14px}

/* sponsors */
.sponsor{position:absolute;font-family:"Didact Gothic",sans-serif;color:var(--deep);font-size:25px;line-height:30px;text-align:center;transform:translateX(-50%);white-space:nowrap}
</style>
</head>
<body>

<div class="abs title-frame"></div>
<div class="art ribbon" role="img" aria-label="Large pink awareness ribbon"></div>
<h1 class="abs title">BREAST CANCER<br>AWARENESS</h1>

<div class="art women" role="img" aria-label="Eight women figures, one highlighted in dark magenta"></div>
<div class="abs big-ratio">1 OUT OF 8</div>
<p class="abs stat-text ratio-text">Women will be<br>diagnosed with breast<br>cancer in their lifetime.</p>

<div class="abs divider-v"></div>
<div class="art world-map" role="img" aria-label="Striped world map"></div>

<div class="abs stat stat-a">
  <div class="every">EVERY</div>
  <div class="num">2</div>
  <div class="unit">MINUTES</div>
  <p class="stat-text">a case of<br>breast<br>cancer is<br>diagnosed.</p>
</div>
<div class="abs stat stat-b">
  <div class="every">EVERY</div>
  <div class="num">13</div>
  <div class="unit">MINUTES</div>
  <p class="stat-text">a woman<br>dies of<br>breast<br>cancer in<br>the USA.</p>
</div>
<div class="art flag" role="img" aria-label="United States flag"></div>
<p class="abs stat-text flag-text">Breast cancer is<br>the most common<br>cancer for women<br>in the USA.</p>

<div class="abs rule" style="top:1252px"></div>
<h2 class="abs section-title" style="top:1293px">RISK FACTORS</h2>

<div class="icon" style="left:93px;top:1403px;width:64px;height:78px" role="img" aria-label="Beer mug icon"></div>
<div class="abs item" style="left:190px;top:1394px"><h3>Alcohol</h3><p>Regular alcohol consumption<br>increases the risk of breast<br>cancer.</p></div>
<div class="icon" style="left:100px;top:1530px;width:50px;height:110px" role="img" aria-label="Female figure icon"></div>
<div class="abs item" style="left:190px;top:1541px"><h3>Being Female</h3><p>Women are at far greater<br>risk than men.</p></div>
<div class="icon" style="left:100px;top:1670px;width:52px;height:104px" role="img" aria-label="Overweight figure icon"></div>
<div class="abs item" style="left:190px;top:1659px"><h3>Obesity</h3><p>Excess body weight,<br>especially after menopause,<br>heightens risk.</p></div>

<div class="icon" style="left:613px;top:1415px;width:92px;height:92px;border-radius:50%" role="img" aria-label="Radiation symbol icon"></div>
<div class="abs item" style="left:764px;top:1394px"><h3>Radiation</h3><p>Previous radiation exposure,<br>especially to the chest, can<br>raise risk.</p></div>
<div class="icon" style="left:590px;top:1576px;width:138px;height:28px" role="img" aria-label="DNA strand icon"></div>
<div class="abs item" style="left:764px;top:1537px"><h3>Genetic</h3><p>Family history and genetic<br>mutations (BRCA1/2)<br>increase risk.</p></div>
<div class="icon" style="left:597px;top:1672px;width:124px;height:100px" role="img" aria-label="Three female figures of different ages"></div>
<div class="abs item" style="left:764px;top:1681px"><h3>Aging</h3><p>The risk of breast cancer<br>rises as women grow older.</p></div>

<div class="abs rule" style="top:1829px"></div>
<h2 class="abs section-title" style="top:1866px">PREVENTION TIPS</h2>

<div class="icon" style="left:93px;top:1990px;width:118px;height:116px" role="img" aria-label="Doctor with stethoscope icon"></div>
<div class="abs item" style="left:249px;top:1986px"><h3>Ask Your Doctor</h3><p>Discuss your risk factors<br>and schedule regular<br>screenings.</p></div>
<div class="icon" style="left:90px;top:2160px;width:102px;height:116px" role="img" aria-label="Crossed-out beer mug icon"></div>
<div class="abs item" style="left:249px;top:2174px"><h3>Drink Less Alcohol</h3><p>Reducing alcohol<br>intake lowers your risk.</p></div>
<div class="icon" style="left:84px;top:2350px;width:130px;height:125px" role="img" aria-label="Two figures showing weight change"></div>
<div class="abs item" style="left:249px;top:2325px"><h3>Maintain Healthy<br>Weight</h3><p>Aim for a healthy body<br>weight through diet<br>and lifestyle.</p></div>

<div class="icon" style="left:598px;top:2020px;width:136px;height:38px" role="img" aria-label="Dumbbell icon"></div>
<div class="abs item" style="left:768px;top:1986px"><h3>Exercise</h3><p>Stay active—regular<br>exercise helps reduce risk.</p></div>
<div class="icon" style="left:598px;top:2148px;width:130px;height:110px" role="img" aria-label="Plate with fork and spoon icon"></div>
<div class="abs item" style="left:768px;top:2135px"><h3>Choose Healthy Diet</h3><p>A balanced diet rich in<br>fruits, vegetables, and<br>whole grains supports<br>prevention.</p></div>
<div class="icon" style="left:600px;top:2345px;width:106px;height:106px;transform:rotate(45deg) scaleX(.35)" role="img" aria-label="Syringe icon"></div>
<div class="abs item" style="left:768px;top:2325px"><h3>Limit<br>Post-Menopausal<br>Hormone Therapy</h3><p>Use the lowest dose for<br>the shortest time, only<br>when necessary.</p></div>

<div class="sponsor" style="left:200px;top:2607px">Clearbrook Water</div>
<div class="sponsor" style="left:437px;top:2607px">Palm Cove Apparel</div>
<div class="sponsor" style="left:682px;top:2607px">The Lantern Bar</div>
<div class="sponsor" style="left:985px;top:2607px">Wellway Pharmacy</div>
<div class="sponsor" style="left:300px;top:2730px">Ridgeline Springs</div>
<div class="sponsor" style="left:560px;top:2730px">Corvale Medical</div>
<div class="sponsor" style="left:800px;top:2730px">Daybright Pharmacy</div>
<div class="sponsor" style="left:1010px;top:2730px">Orchard Lane</div>

</body>
</html>
```